Far-Ridge Brokerage Business Cards

We have had success with our logo design and are looking to have a creative business card made. Logo must be prominent in the business card design. We would like headshots to be on the business card, but do not want the photo to be framed at all. We are looking for designs for two different people, so I will attach headshots

Target Market(s)

Home Buyers. Trying to market to younger/trendy crowd. 25-45 year of age.

Industry/Entity Type

Real Estate

Contact Information for Business Card

New business card design needed. Looking for a vibrant and attractive business card.

Font styles to use
Other font styles liked:
• Match the logo font on the Far-Ridge PDQ Realty logo

Requirements
Must have
• Must have sketch swarm logo incorporated. Fair Dwelling Logo should be very small and should be on the back of the card and is a requirement. Propertist logo should be small and on the back of the card with FD logo.

2 different business cards, must have the following info:
Business card 1:
Gary Pelloway & Marla Ventrisch
(555) 208-4417
Marla@frp.example
Marla.lakeviewdwellingsonmarket.example
7283 W Larchmere St, Brindlefield, WI 53999

Business card 2:
Dominic Varseth
(555) 734-2190
Dom@frp.example
Dominic.lakeviewdwellingsonmarket.example

```html
<!DOCTYPE html>
<html lang="en">
<head>
<meta charset="utf-8">
<title>Far-Ridge PDQ Realty — Business Card</title>
<link rel="stylesheet" href="https://fonts.googleapis.com/css2?family=Montserrat:wght@400;500;700;800&display=swap">
<style>
  :root {
    --stage: #e4e4e4;
    --navy: #0b1f3f;
    --navy-deep: #081831;
    --edge: #e99b1c;
    --sky: #2b9be0;
    --white: #ffffff;
    --silver: #c9ccd1;
    --photo-light: #c9c7c4;
    --photo-dark: #1a2a47;
  }
  * { box-sizing: border-box; margin: 0; padding: 0; }
  html, body { width: 1200px; height: 800px; overflow: hidden; }
  body {
    background: var(--stage);
    font-family: "Montserrat", Arial, sans-serif;
    display: flex;
    align-items: center;
    justify-content: center;
    gap: 40px;
  }
  .card {
    position: relative;
    width: 540px;
    height: 309px;
    border-radius: 18px;
    background: var(--navy);
    border-bottom: 3px solid var(--edge);
    overflow: hidden;
  }
  /* front */
  .headshot {
    position: absolute;
    right: 0;
    top: 0;
    width: 250px;
    height: 306px;
    background: radial-gradient(ellipse at 50% 55%, var(--photo-light) 0%, #8d8d8f 45%, var(--photo-dark) 75%, var(--navy) 100%);
  }
  .front-info {
    position: absolute;
    left: 34px;
    top: 52px;
    width: 290px;
  }
  .brand {
    display: flex;
    align-items: center;
    gap: 10px;
    margin-bottom: 26px;
  }
  .brand-dot {
    width: 34px;
    height: 34px;
    border-radius: 50%;
    background: var(--edge);
    flex: none;
  }
  .brand-name {
    color: var(--white);
    font-weight: 700;
    font-size: 20px;
    letter-spacing: 1px;
    text-transform: uppercase;
    line-height: 1.1;
  }
  .agent-name {
    color: var(--sky);
    font-weight: 800;
    font-size: 25px;
    margin-bottom: 12px;
  }
  .contact-list { list-style: none; }
  .contact-list li {
    display: flex;
    align-items: center;
    gap: 7px;
    color: var(--white);
    font-size: 10.5px;
    font-weight: 500;
    line-height: 1.75;
    white-space: nowrap;
  }
  .contact-list svg { width: 10px; height: 10px; flex: none; fill: var(--sky); }
  .contact-row { display: flex; gap: 14px; }
  /* back */
  .card-back {
    display: flex;
    flex-direction: column;
    align-items: center;
    justify-content: center;
    gap: 26px;
  }
  .back-brand { display: flex; align-items: center; gap: 14px; }
  .back-brand .brand-dot { width: 44px; height: 44px; background: var(--silver); }
  .back-brand .brand-name { color: var(--silver); font-size: 28px; }
  .badges { display: flex; gap: 8px; }
  .badge { width: 22px; height: 22px; background: var(--silver); }
</style>
</head>
<body>
  <article class="card card-front">
    <div class="headshot" role="img" aria-label="Agent headshot, unframed, smiling man in a grey quarter-zip sweater"></div>
    <div class="front-info">
      <div class="brand">
        <span class="brand-dot"></span>
        <span class="brand-name">Far-Ridge PDQ Realty</span>
      </div>
      <h1 class="agent-name">Dominic Varseth</h1>
      <ul class="contact-list">
        <li class="contact-row">
          <span style="display:flex;align-items:center;gap:7px">
            <svg viewBox="0 0 24 24"><path d="M6.6 10.8a15.1 15.1 0 0 0 6.6 6.6l2.2-2.2c.3-.3.7-.4 1-.2 1.1.4 2.3.6 3.6.6.6 0 1 .4 1 1V20c0 .6-.4 1-1 1A17 17 0 0 1 3 4c0-.6.4-1 1-1h3.5c.6 0 1 .4 1 1 0 1.3.2 2.5.6 3.6.1.3 0 .7-.2 1z"/></svg>
            (555) 734-2190
          </span>
          <span style="display:flex;align-items:center;gap:7px">
            <svg viewBox="0 0 24 24"><path d="M2 5h20v14H2z M2 5l10 8 10-8" fill="none" stroke="#2b9be0" stroke-width="2.4"/></svg>
            Dom@frp.example
          </span>
        </li>
        <li>
          <svg viewBox="0 0 24 24"><circle cx="12" cy="12" r="10" fill="none" stroke="#2b9be0" stroke-width="2.4"/><path d="M2 12h20M12 2c3 3 3 17 0 20M12 2c-3 3-3 17 0 20" fill="none" stroke="#2b9be0" stroke-width="1.8"/></svg>
          Dominic.lakeviewdwellingsonmarket.example
        </li>
        <li>
          <svg viewBox="0 0 24 24"><path d="M12 2a7 7 0 0 0-7 7c0 5 7 13 7 13s7-8 7-13a7 7 0 0 0-7-7zm0 9.5a2.5 2.5 0 1 1 0-5 2.5 2.5 0 0 1 0 5z"/></svg>
          7283 W Larchmere St, Brindlefield, WI 53999
        </li>
      </ul>
    </div>
  </article>

  <article class="card card-back">
    <div class="back-brand">
      <span class="brand-dot"></span>
      <span class="brand-name">Far-Ridge PDQ Realty</span>
    </div>
    <div class="badges" aria-label="Propertist and Fair Dwelling badges">
      <span class="badge"></span>
      <span class="badge"></span>
    </div>
  </article>
</body>
</html>
```